Communication and Marketing agency needs a new presentation card

We are a group of communication and marketing agencies specialized in companies that are in the logistics and industrial sector. The head agency is TELVANO Grupo and the group consists of 4 agencies: TELVANO Media, TELVANO Digital, TELVANO Research and EnlazaPorImagen. We hace 4 offices in Spain (Madrid, Barcelona, Valencia and Murcia). We are looking for a clean and attractive design that transmits our experience, brand presence in the market and knowledge to those who receive the card.It has to maintain the colors of the logo that is attached.
Target Market(s)
logistics and industrial sector
Marketing department
Clean and attractive design

```html
<!DOCTYPE html>
<html lang="es">
<head>
<meta charset="utf-8">
<title>TELVANO Grupo – Tarjeta de presentación</title>
<link rel="stylesheet" href="https://fonts.googleapis.com/css2?family=Roboto:wght@400;500;700&display=swap">
<style>
  :root {
    --brand-red: #b31b27;
    --ink: #1c1c1c;
    --ink-soft: #4a4a4a;
    --rule: #8a8a8a;
    --paper: #ffffff;
    --backdrop: #e4e4e4;
  }
  * { margin: 0; padding: 0; box-sizing: border-box; }
  html, body {
    width: 1125px; height: 1200px; overflow: hidden;
    background: var(--backdrop);
    font-family: "Roboto", Arial, sans-serif;
  }
  .stage {
    position: relative; width: 1090px; height: 1163px;
    transform: scale(1.0321); transform-origin: 0 0;
  }
  .card {
    position: absolute; left: 166px; width: 800px; height: 457px;
    box-shadow: 0 2px 4px rgba(0,0,0,.25);
  }
  .card--front { top: 103px; background: var(--paper); }
  .card--back { top: 619px; background: var(--brand-red); }

  /* wordmark */
  .wordmark {
    position: absolute; display: flex; flex-direction: column; align-items: flex-end;
    font-weight: 500; line-height: 1;
  }
  .wordmark__name { letter-spacing: 2px; }
  .card--front .wordmark { right: 43px; top: 58px; color: var(--brand-red); }
  .card--front .wordmark__name { font-size: 58px; }
  .card--front .wordmark__unit { font-size: 34px; margin-top: 4px; }

  .card--back .wordmark--lead { left: 180px; width: 412px; top: 158px; color: var(--paper); }
  .card--back .wordmark--lead .wordmark__name { font-size: 84px; letter-spacing: 4px; }
  .card--back .wordmark--lead .wordmark__unit { font-size: 48px; margin-top: 6px; }

  /* holder */
  .holder__bar { position: absolute; left: 0; top: 202px; width: 18px; height: 50px; background: var(--brand-red); }
  .holder__name { position: absolute; left: 42px; top: 200px; font-size: 28px; font-weight: 700; color: var(--brand-red); }
  .holder__role { position: absolute; left: 43px; top: 233px; font-size: 19px; font-weight: 500; color: var(--ink); }
  .divider { position: absolute; left: 42px; right: 43px; top: 270px; height: 1px; background: var(--rule); }

  .contact { position: absolute; left: 42px; top: 290px; list-style: none; }
  .contact li { display: flex; align-items: center; height: 25.5px; font-size: 19px; color: var(--ink-soft); }
  .contact svg { width: 18px; height: 18px; margin-right: 11px; fill: var(--brand-red); flex: none; }

  .offices { position: absolute; right: 42px; top: 316px; list-style: none; text-align: right; }
  .offices li { height: 25.5px; line-height: 25.5px; font-size: 19px; color: var(--ink-soft); }
  .offices li::after {
    content: ""; display: inline-block; width: 5px; height: 5px; border-radius: 50%;
    background: var(--brand-red); margin-left: 9px; vertical-align: middle;
  }

  /* back */
  .back__rule { position: absolute; left: 30px; right: 32px; top: 352px; height: 1px; background: rgba(255,255,255,.85); }
  .agencies { position: absolute; left: 30px; right: 32px; top: 381px; display: flex; justify-content: space-between; }
  .agency { display: flex; flex-direction: column; align-items: flex-end; color: var(--paper); font-weight: 500; line-height: 1; }
  .agency__name { font-size: 27px; letter-spacing: 1px; }
  .agency__unit { font-size: 18px; margin-top: 3px; }
  .agency--stacked { align-items: flex-start; }
  .agency--stacked .agency__name { font-size: 24px; letter-spacing: 1px; }
</style>
</head>
<body>
<div class="stage">

  <section class="card card--front">
    <div class="wordmark">
      <span class="wordmark__name">TELVANO</span>
      <span class="wordmark__unit">Media</span>
    </div>

    <div class="holder__bar"></div>
    <h1 class="holder__name">Lucía Ortega</h1>
    <p class="holder__role">Director</p>
    <div class="divider"></div>

    <ul class="contact">
      <li><svg viewBox="0 0 24 24"><path d="M6.6 10.8a15.2 15.2 0 0 0 6.6 6.6l2.2-2.2c.3-.3.7-.4 1-.2 1.1.4 2.3.6 3.6.6.6 0 1 .4 1 1V20c0 .6-.4 1-1 1A17 17 0 0 1 3 4c0-.6.4-1 1-1h3.5c.6 0 1 .4 1 1 0 1.3.2 2.5.6 3.6.1.3 0 .7-.2 1z"/></svg>910 472 318</li>
      <li><svg viewBox="0 0 24 24"><path d="M7 1h10a2 2 0 0 1 2 2v18a2 2 0 0 1-2 2H7a2 2 0 0 1-2-2V3a2 2 0 0 1 2-2zm0 3v14h10V4zm5 15.5a1.2 1.2 0 1 0 0 2.4 1.2 1.2 0 0 0 0-2.4z"/></svg>655 281 447</li>
      <li><svg viewBox="0 0 24 24"><path d="M2 5h20v14H2zm2 2v.4l8 5.2 8-5.2V7zm0 2.8V17h16V9.8l-8 5.2z"/></svg>lortega@telvano.es</li>
      <li><svg viewBox="0 0 24 24"><rect x="3" y="3" width="18" height="18" rx="2"/></svg>luciaortega</li>
      <li><svg viewBox="0 0 24 24"><path d="M12 2a10 10 0 1 0 0 20 10 10 0 0 0 0-20zm-1 17.9A8 8 0 0 1 4.2 10.2L9 15v1a2 2 0 0 0 2 2zm6.9-2.5A2 2 0 0 0 16 16h-1v-3a1 1 0 0 0-1-1H8v-2h2a1 1 0 0 0 1-1V7h2a2 2 0 0 0 2-2v-.4a8 8 0 0 1 2.9 12.8z"/></svg>www.telvano.es</li>
    </ul>

    <ul class="offices">
      <li>Madrid</li>
      <li>Barcelona</li>
      <li>Valencia</li>
      <li>Murcia</li>
    </ul>
  </section>

  <section class="card card--back">
    <div class="wordmark wordmark--lead">
      <span class="wordmark__name">TELVANO</span>
      <span class="wordmark__unit">Grupo</span>
    </div>

    <div class="back__rule"></div>

    <div class="agencies">
      <div class="agency"><span class="agency__name">TELVANO</span><span class="agency__unit">Digital</span></div>
      <div class="agency"><span class="agency__name">TELVANO</span><span class="agency__unit">Media</span></div>
      <div class="agency"><span class="agency__name">TELVANO</span><span class="agency__unit">Research</span></div>
      <div class="agency agency--stacked"><span class="agency__name">ENLAZA</span><span class="agency__name">PORIMAGEN</span></div>
    </div>
  </section>

</div>
</body>
</html>
```